Heritage Hollow Business Cards

Require a business card design. <br/><br/>Needs to include logo (either round or long version) plus these details:<br/>Maya Torvel<br/>Heritage Hollow<br/>maya@quonbrook.com.au<br/>02 6481 7390<br/>PO Box Glenwarra NSW 2913<br/>www.heritagehollow.com.au<br/><br/>I need in an editable format so that I can create for multiple staff members. <br/><br/>

Target Market(s)

We are an online store selling renovation products to home owners are builders. Looking for a classic classy design.

Industry/Entity Type

Home And Garden

Contact Information for Business Card

Maya Torvel
Heritage Hollow
maya@quonbrook.com.au
02 6481 7390
PO Box Glenwarra NSW 2913
www.heritagehollow.com.au

Colors

Designer to choose colors to be used in the design.

Requirements
Must have
• Must include Logo.

```html
<!DOCTYPE html>
<html lang="en">
<head>
<meta charset="utf-8">
<title>Heritage Hollow Business Cards</title>
<link href="https://fonts.googleapis.com/css2?family=Lato:wght@400;700;900&display=swap" rel="stylesheet">
<style>
  :root {
    --backdrop: #2b2b2b;
    --card-black: #050505;
    --card-white: #ffffff;
    --ink: #111111;
    --ink-soft: #333333;
    --rule: #8a8a8a;
    --accent-grey: #6a6a6a;
    --paper-text: #f2f2f2;
  }
  * { margin: 0; padding: 0; box-sizing: border-box; }
  html, body {
    width: 1200px; height: 878px; overflow: hidden;
    background: var(--backdrop);
    font-family: "Lato", sans-serif;
  }
  .canvas { position: relative; width: 1200px; height: 878px; }

  .card {
    position: absolute;
    width: 600px; height: 340px;
    box-shadow: 0 14px 30px rgba(0,0,0,0.55);
  }

  /* Front (black) */
  .card-front {
    left: 460px; top: 60px;
    background: var(--card-black);
    display: flex; align-items: center; justify-content: center;
  }
  .front-logo {
    display: flex; align-items: center; gap: 14px;
    color: var(--paper-text);
    font-weight: 700; font-size: 40px; letter-spacing: 0.5px;
  }
  .logo-dot {
    width: 44px; height: 44px; border-radius: 50%;
    border: 2px solid var(--paper-text);
  }

  /* Back (white) */
  .card-back {
    left: 150px; top: 480px;
    background: var(--card-white);
    color: var(--ink);
  }
  .holder-name {
    position: absolute; left: 34px; top: 34px;
    font-weight: 900; font-size: 30px;
  }
  .holder-company {
    position: absolute; left: 34px; top: 74px;
    font-size: 17px; color: var(--ink-soft);
  }
  .contact-list {
    position: absolute; left: 34px; top: 196px;
    list-style: none;
    font-size: 18px; color: var(--ink-soft);
  }
  .contact-list li {
    display: flex; align-items: center; gap: 12px;
    height: 26px;
  }
  .contact-list svg { width: 15px; height: 15px; flex: none; }
  .contact-list .address { margin-top: 6px; font-size: 19px; }
  .bottom-rule {
    position: absolute; left: 34px; right: 30px; top: 310px;
    height: 1px; background: var(--rule);
  }
  .side-tab {
    position: absolute; left: 0; top: 278px;
    width: 24px; height: 14px; background: var(--accent-grey);
  }
  .back-logo {
    position: absolute; right: 40px; top: 150px;
    width: 240px;
    display: flex; align-items: center; gap: 12px;
    font-weight: 700; font-size: 30px; line-height: 1.05;
    color: var(--ink);
  }
  .back-logo .logo-dot { border-color: var(--ink); width: 36px; height: 36px; }
</style>
</head>
<body>
<main class="canvas">
  <section class="card card-front" aria-label="Card front">
    <div class="front-logo">
      <span class="logo-dot"></span>
      <span class="logo-name">Heritage Hollow</span>
    </div>
  </section>

  <section class="card card-back" aria-label="Card back">
    <h1 class="holder-name">Maya Torvel</h1>
    <p class="holder-company">Heritage Hollow</p>

    <ul class="contact-list">
      <li>
        <svg viewBox="0 0 16 16"><path d="M4 1.5l2.3 3-1.4 1.6a8 8 0 0 0 5 5l1.6-1.4 3 2.3-1.6 2.4C6.8 14 2 9.2 1.6 3.1z" fill="#222"/></svg>
        02 6481 7390
      </li>
      <li>
        <svg viewBox="0 0 16 16"><rect x="1" y="3.5" width="14" height="9" fill="#222"/><path d="M1 3.5l7 5 7-5" stroke="#fff" stroke-width="1.2" fill="none"/></svg>
        maya@quonbrook.com.au
      </li>
      <li>
        <svg viewBox="0 0 16 16"><circle cx="8" cy="8" r="6.5" stroke="#222" stroke-width="1.4" fill="none"/><path d="M1.5 8h13M8 1.5c-3 3.5-3 9.5 0 13M8 1.5c3 3.5 3 9.5 0 13" stroke="#222" stroke-width="1.1" fill="none"/></svg>
        www.heritagehollow.com.au
      </li>
      <li class="address">
        <svg viewBox="0 0 16 16"><path d="M8 1a5 5 0 0 1 5 5c0 4-5 9-5 9S3 10 3 6a5 5 0 0 1 5-5z" fill="#222"/><circle cx="8" cy="6" r="1.8" fill="#fff"/></svg>
        PO Box Glenwarra NSW 2913
      </li>
    </ul>

    <div class="bottom-rule"></div>
    <div class="side-tab"></div>

    <div class="back-logo">
      <span class="logo-dot"></span>
      <span class="logo-name">Heritage Hollow</span>
    </div>
  </section>
</main>
</body>
</html>
```